Lotven Pharma Chinese Traditional Medicine Web Design

We need a web design for a new company based in Shanghai China called 'Lotven Pharma'. We develop Chinese traditional herbal medicine, including research and development, technical support service, manufacturing, . Also, there’s a small ratio of western medicine. Our goal is to contributing to a healthier future.

Target Market(s)

global,but mainly China

Industry/Entity Type

Pharmaceutical

Number of Pages Required

1 page

Font styles to use
Serif

Colors
e4daeb
cedeed
cadf82
eaf2ce
fbd4d5
fee3d4
fabb94
fee18a
b8a6cd

Requirements
Must have
• triditional Chinese elements, concept of herbal, health, value, better life for people..could be colourful but not more than 3 different colour..
Nice to have
• Style: simple, communicate traditional Chinese herbal medicine element, as well as modern technique..same as LOGO style..
Should not have
• please dont show more IT elements...

```html
<!DOCTYPE html>
<html lang="zh">
<head>
<meta charset="utf-8">
<title>Lotven Pharma 洛文医药</title>
<link href="https://fonts.googleapis.com/css2?family=Noto+Sans+SC:wght@500;700&family=Noto+Serif+SC:wght@400;500&family=Roboto:wght@500&display=swap" rel="stylesheet">
<style>
:root{
  --brown:#7a4a2e;
  --blush:#fbece4;
  --white:#ffffff;
  --leaf:#5c8a4a;
  --footer-text:#f4f1ec;
}
*{margin:0;padding:0;box-sizing:border-box}
html,body{width:1014px;height:1200px;overflow:hidden}
body{position:relative;background:var(--white);font-family:"Noto Sans SC",sans-serif;color:var(--brown)}
.page-band{position:absolute;left:0;top:337px;width:1014px;height:863px;background:var(--blush)}
.brand{position:absolute;top:54px;left:0;width:1014px;text-align:center;font-family:"Noto Serif SC",serif;color:var(--brown)}
.brand-name{font-size:17px;font-weight:500;letter-spacing:.5px;display:inline-flex;align-items:center;gap:8px}
.brand-dot{width:10px;height:10px;border-radius:50%;background:var(--brown);display:inline-block}
.brand-sub{font-size:10px;margin-top:2px;letter-spacing:2px}
.main-nav{position:absolute;top:126px;left:0;width:1014px;height:16px;font-family:"Roboto",sans-serif;font-size:9.5px;font-weight:500;color:var(--brown)}
.main-nav a{position:absolute;white-space:nowrap;color:inherit;text-decoration:none}
.nav-home{left:150px;top:4px}
.nav-company{left:268px;top:3px}
.nav-news{left:427px;top:2px}
.nav-products{left:518px;top:1px}
.nav-career{left:695px;top:0}
.nav-contact{left:802px;top:-1px}
.hero{position:absolute;left:107px;top:170px;width:799px;height:345px;border-radius:8px;overflow:hidden;
  background:linear-gradient(180deg,#efe6dc 0%,#cdd9a8 28%,#a8c67c 55%,#86ad5a 80%,#7ea24f 100%)}
.hero-title{position:absolute;top:155px;left:0;width:100%;text-align:center;font-size:20.5px;font-weight:700;color:#8a4a28;letter-spacing:.3px}
.card{position:absolute;top:548px;width:384px;height:329px;background:var(--white);border-radius:6px;box-shadow:0 1px 6px rgba(120,80,50,.08)}
.card-intro{left:107px}
.card-news{left:523px}
.card h2{font-size:16px;font-weight:700;text-align:center;margin-top:38px;color:var(--brown)}
.intro-list{list-style:none;margin-top:44px;text-align:center;font-size:12px;font-weight:700;color:var(--brown)}
.intro-list li{height:44px}
.news-list{list-style:none;margin-top:17px;padding-left:30px;font-size:12px;font-weight:700;color:var(--brown)}
.news-list li{display:flex;align-items:center;gap:10px;height:44px}
.news-list svg{width:26px;height:26px;flex:none}
.footer{position:absolute;left:0;top:905px;width:1014px;height:295px;
  background:linear-gradient(180deg,var(--blush) 0%,#b9b5a4 25%,#7d816b 55%,#4e5a43 100%)}
.footer-links,.footer-info{position:absolute;top:60px;font-size:15.5px;font-weight:700;line-height:24.7px;color:var(--footer-text)}
.footer-links{left:107px;list-style:none}
.footer-info{left:523px;width:250px}
.footer-dot{position:absolute;left:143px;width:6px;height:6px;border:1px solid var(--footer-text);border-radius:50%}
</style>
</head>
<body>
<div class="page-band"></div>

<header class="brand">
  <div class="brand-name"><span class="brand-dot"></span>LOTVEN PHARMA</div>
  <div class="brand-sub">洛文医药</div>
</header>

<nav class="main-nav">
  <a class="nav-home" href="#">HOMEPAGE</a>
  <a class="nav-company" href="#">COMPANY OVERALL</a>
  <a class="nav-news" href="#">NEWS</a>
  <a class="nav-products" href="#">PRODUCTS &amp; SERVICES</a>
  <a class="nav-career" href="#">CAREER</a>
  <a class="nav-contact" href="#">CONTACT US</a>
</nav>

<section class="hero" role="img" aria-label="Sunlit meadow of green herbs and small white wildflowers">
  <p class="hero-title">公司首页公司首页公司首页公司首页公司首页</p>
</section>

<section class="card card-intro">
  <h2>公司简介</h2>
  <ul class="intro-list">
    <li>公司首页公司首页公司首页公司首页公司首页</li>
    <li>公司首页公司首页公司首页公司首页公司首页</li>
    <li>公司首页公司首页公司首页公司首页公司首页</li>
  </ul>
</section>

<section class="card card-news">
  <h2>公司新闻</h2>
  <ul class="news-list">
    <li><svg viewBox="0 0 26 26" fill="none" stroke="var(--leaf)" stroke-width="1"><path d="M4 22 C4 12 10 5 22 4 C21 15 14 21 4 22Z"/><path d="M2 24 L16 10"/><path d="M9 17 L9 12 M12 14 L16 14"/></svg>公司首页公司首页公司首页公司首页公司首页</li>
    <li><svg viewBox="0 0 26 26" fill="none" stroke="var(--leaf)" stroke-width="1"><path d="M4 22 C4 12 10 5 22 4 C21 15 14 21 4 22Z"/><path d="M2 24 L16 10"/><path d="M9 17 L9 12 M12 14 L16 14"/></svg>公司首页公司首页公司首页公司首页公司首页</li>
    <li><svg viewBox="0 0 26 26" fill="none" stroke="var(--leaf)" stroke-width="1"><path d="M4 22 C4 12 10 5 22 4 C21 15 14 21 4 22Z"/><path d="M2 24 L16 10"/><path d="M9 17 L9 12 M12 14 L16 14"/></svg>公司首页公司首页公司首页公司首页公司首页</li>
    <li><svg viewBox="0 0 26 26" fill="none" stroke="var(--leaf)" stroke-width="1"><path d="M4 22 C4 12 10 5 22 4 C21 15 14 21 4 22Z"/><path d="M2 24 L16 10"/><path d="M9 17 L9 12 M12 14 L16 14"/></svg>公司首页公司首页公司首页公司首页公司首页</li>
    <li><svg viewBox="0 0 26 26" fill="none" stroke="var(--leaf)" stroke-width="1"><path d="M4 22 C4 12 10 5 22 4 C21 15 14 21 4 22Z"/><path d="M2 24 L16 10"/><path d="M9 17 L9 12 M12 14 L16 14"/></svg>公司首页公司首页公司首页公司首页公司首页</li>
  </ul>
</section>

<footer class="footer" role="img" aria-label="Misty tangle of herb roots and small green leaves">
  <span class="footer-dot" style="top:44px"></span>
  <ul class="footer-links">
    <li>青禾本草健康产业发展联合会</li>
    <li>松岚中药材种植合作联盟</li>
    <li>云溪草本标准研究中心</li>
    <li>澄川医药健康进出口协会</li>
    <li>远山本草学会</li>
    <li>岚溪本草植物研究院</li>
    <li>青禾药用植物资源研究所</li>
  </ul>
  <span class="footer-dot" style="top:242px"></span>
  <p class="footer-info">company name（洛文医药（上海）有限公司）<br>company address（中国（上海）自由贸易试验区青禾路128号）<br>registration no.（沪公网安备31000000000000号）</p>
</footer>
</body>
</html>
```